Colourful Bold Design for Pet Insurance Website

PLEASE NOTE THAT THIS PROJECT HAS BEEN EXTENDED. Please read the PROJECT EXTENSION DOCUMENT BEFORE STARTING WORK ON ANY DESIGNS.

We are looking for a colourful bold new template design for our JOOMLA HOMEPAGE and a matching design for our new WORDPRESS BLOG.

The website will help pet owners work out which insurance policy best meets their needs. The aim of the website is to explain policy differences in a plain clear manner.

The website will need to have a professional colourful image. It needs to be BOLD, CLEAN AND SHARP rather than soft, pastel and cuddly.

COLOUR SCHEME
The website needs to have a bold colourful design on a white background.
On the inner pages we will have five different types of policies which will be colour coded. We would ideally therefore like to incorporate five distinct colours in the design. See attached document for example of colour schemes we like.

LOGO
We want to keep the existing logo. Please find the file attached. You may though change the logo colours.

CONTENT
One of the reasons for the new design is that we want to change the style of the homepage and include new content. Our current homepage can be found at www.furrow-cover-polls.co.uk.

Content Required
Slideshow
Article Intro.. About Pet Insurance
Policy Lookup Box (see existing site… you can change the design of this)
Six link options (see links on left of current page)
Latest Reviews (List of 6)
Ad (Same dimensions as currently on homepage)

News and Comment Section - To include Three or Four Articles, Title, Intro to article (probably 3 or 4 lines .. about 400px wide), Read more link
Social Media Section
Chatterbook Plugin with Feed
Latest Tweets Plugin
Pet Charities Latest Tweets
Footer
Larger footer with lots of links grouped in sections

It does not need to include the clipart pic of the pets which is on the current homepage.

Examples of Websites and Templates We Like
http://www.pawlane.com/ (like colours… fonts…layout)
http://sitetheme.brightkiln.com/?template=upbeat&path=/... (like the clarity, "white" space etc)
http://www.layoutforge.com/demo/51872.html (like white space, clear easy to read fonts… don’t like colour scheme, size of top picture)
http://www.layoutforge.com/website-templates/63915.html (like colour scheme, use of white space)

FEEDBACK
I will provide lots of feedback on all designs submitted so that together we can get the best result.

For clarification this is a DESIGN ONLY project. Our website developer will view the designs before we make our final choice as he wants to ensure he can develop "sharp, practical and most importantly light weight web interface" from the design.

Just updated this brief to clarify design issues, content issues and to give some more examples of site designs I like. 

Please note that although we wish to keep the logo you can change the colours to suit your design. 

Please note that we have now added details of pictures we would be happy to use on the website.  We would prefer it if you used one of these.   Otherwise please ensure your picture includes a nice dog and nice cat and no people!

I have been delighted with the quality of the designs submitted for this project.  So much so that I am going to extend the project to include some additional inner pages.   The amended brief will be posted on here on Friday 10 May.   The deadline will be extended and the budget will also be increased. 

Reason: Additional inner pages now required. Budget will be increased. Revised brief to be posted on here Friday 10 May.

Target Market(s)

Pet owners in the UK who are confused about pet insurance. It therefore needs to be a bold design which is plain, clean and easy to read. It should use bold colours rather than pastels and should not use "cuddly" images.

Industry/Entity Type

Insurance

Requirements
Must have
• Bold clear and distinct colours (preferably 5)
Content as per uploaded file (not just content from existing site)
Easy to read fonts
Should not have
• Pastel colours
Cuddly images

```html
<!DOCTYPE html>
<html lang="en">
<head>
<meta charset="utf-8">
<title>Furrow Cover Polls UK</title>
<link rel="stylesheet" href="https://fonts.googleapis.com/css2?family=Ubuntu:wght@400;500&family=Arimo:wght@400;700&display=swap">
<style>
:root{
  --page-top:#efedec;
  --page-mid:#e2e2e2;
  --white:#ffffff;
  --ink:#333333;
  --muted:#555555;
  --blue:#1a78c2;
  --orange:#f07a1f;
  --purple:#8f44c9;
  --green:#5fb56e;
  --grey:#8a8a8a;
  --brand-blue:#2a86c8;
  --brand-green:#6cbf3a;
  --footer:#8e8e8e;
  --footer-dark:#6d6d6d;
  --footer-text:#f4f4f4;
  --panel:#f4f2f2;
  --line:#d8d8d8;
  --tweet-date:#7ee08a;
}
*{box-sizing:border-box;margin:0;padding:0}
html,body{width:768px;height:1200px;overflow:hidden}
body{position:relative;background:linear-gradient(var(--page-top) 0 84px,var(--page-mid) 84px);font-family:"Arimo",Arial,sans-serif;color:var(--ink)}
.abs{position:absolute}
.sheet{left:96px;top:16px;width:576px;height:808px;background:var(--white);box-shadow:0 0 6px rgba(0,0,0,.25)}
.brand{left:115px;top:32px;display:flex;align-items:center;gap:8px}
.brand-mark{width:44px;height:44px;background:var(--brand-green);border-radius:50%}
.brand-name{font-family:"Ubuntu",sans-serif;font-size:20px;line-height:20px;color:var(--brand-blue)}
.search{left:437px;top:45px;width:222px;height:22px;border:1px solid #bbb;border-radius:3px;background:#fff;box-shadow:inset 0 1px 2px rgba(0,0,0,.2)}
.search-btn{position:absolute;right:1px;top:1px;width:51px;height:18px;background:var(--brand-blue);color:#fff;font-size:10px;text-align:center;line-height:18px;border-radius:2px}
.nav-bars{left:101px;top:96px;width:566px;height:3px;display:flex;gap:2px}
.nav-bars span{flex:1}
.nav{left:101px;top:108px;width:566px;display:flex;justify-content:space-between;padding:0 16px 0 17px;font-family:"Ubuntu",sans-serif;font-size:10px;color:#555}
.nav .current{color:var(--blue)}
.nav-rule{left:101px;top:130px;width:566px;height:1px;background:#e4e4e4}
.slider{left:101px;top:133px;width:566px;height:180px;background:linear-gradient(100deg,#b9a99a,#efe9e2 40%,#9d948c 55%,#f1eeea 80%,#c9bfb4)}
.slider-caption{left:101px;top:291px;width:566px;height:22px;background:rgba(130,130,130,.85);color:#fff;font-size:11.5px;font-weight:700;text-align:center;line-height:22px}
.slider-arrow{top:204px;width:26px;height:26px;border-radius:50%;background:rgba(255,255,255,.85)}
.col-title{font-family:"Ubuntu",sans-serif;font-size:19px;color:#222}
.welcome-img{left:106px;top:362px;width:201px;height:83px;border:1px solid var(--line);background:linear-gradient(90deg,#f6f3ef,#c7b39a 50%,#efeae4)}
.welcome-text{left:106px;top:458px;width:205px;font-size:8.5px;line-height:14px;color:var(--muted)}
.welcome-text p{margin-bottom:14px}
.vrule{width:1px;background:var(--line)}
.links{left:338px;top:362px;list-style:none;font-size:8px;font-weight:700;color:#444}
.links li{height:24px}
.links li::before{content:"»";color:var(--orange);margin-right:4px;font-size:10px}
.select{left:494px;width:164px;height:19px;border:1px solid #ccc;background:#fff;font-size:8px;color:#666;padding:4px 5px}
.select::after{content:"";position:absolute;right:3px;top:3px;width:11px;height:11px;background:#c9d5ea;border:1px solid #9aaecf}
.submit{left:588px;top:425px;width:70px;height:19px;background:var(--green);color:#fff;font-size:9.5px;text-align:center;line-height:19px}
.magnifier{left:494px;top:451px;width:149px;height:149px;background:radial-gradient(circle at 40% 40%,#eef3fa 0 30%,#d7dde3 45%,#fff 70%)}
.hrule{left:106px;top:612px;width:552px;height:1px;background:var(--line)}
.panel{left:106px;top:625px;width:552px;height:188px;background:var(--panel);border:1px solid #e3e1e1}
.reviews{left:120px;top:671px;list-style:none;font-size:8px;font-weight:700;color:#444}
.reviews li{height:24px}
.reviews li::before{content:"";display:inline-block;width:4px;height:4px;border-radius:50%;background:var(--purple);margin:0 8px 1px 2px}
.news{left:253px;top:663px;width:225px;font-size:7.5px;line-height:12.2px;color:#444}
.news h4{color:var(--orange);font-size:8px;margin-bottom:5px}
.news a{color:var(--blue);font-weight:700;text-decoration:none;display:block;margin-bottom:13px}
.news-photo{left:491px;top:645px;width:149px;height:153px;border:1px solid var(--line);background:linear-gradient(#f4f4f4,#a58a6c 60%,#f4f4f4)}
.footer{left:0;top:837px;width:768px;height:363px;background:var(--footer)}
.foot-title{top:856px;font-family:"Ubuntu",sans-serif;font-size:11px;color:#fff}
.fb{left:96px;top:878px;width:176px;height:175px;background:#fff;border:1px solid #aaa;font-size:7px;color:#333}
.fb-head{height:17px;border-bottom:1px solid #ddd;background:#f2f2f2;font-weight:700;padding:4px 6px}
.fb-page{display:flex;gap:6px;padding:7px 6px 4px}
.fb-sq{width:24px;height:24px;background:#3b5a98}
.fb-name{color:#3b5a98;font-weight:700;font-size:8.5px}
.fb-like{margin-top:3px;width:27px;border:1px solid #bbb;font-size:6px;padding:1px 2px;background:#f6f6f6}
.fb-count{padding:2px 6px;border-top:1px solid #eee}
.fb-grid{display:grid;grid-template-columns:repeat(5,30px);gap:3px 4px;padding:3px 6px;text-align:center;font-size:5.5px;color:#555}
.fb-grid i{display:block;height:29px;background:#b9a796}
.fb-foot{position:absolute;bottom:2px;left:6px;font-size:5.5px;color:#555}
.tweets{top:878px;width:177px;height:175px;background:var(--footer-dark);padding:12px 8px 0 9px}
.tweet{display:flex;gap:9px;height:54px;font-size:6.5px;line-height:10.5px;color:#fff}
.tweet svg{flex:none}
.tweet b{font-weight:700}
.tweet em{font-style:normal;color:var(--tweet-date)}
.foot-rule{left:96px;width:576px;height:1px;background:#a9a9a9}
.foot-links{top:1078px;list-style:none;font-size:8.5px;line-height:18px;color:var(--footer-text)}
.follow{left:588px;top:1076px;font-family:"Ubuntu",sans-serif;font-size:10.5px;color:#fff}
.social{left:588px;top:1096px;display:flex;gap:5px}
.social span{width:17px;height:17px;border-radius:50%;background:#bdbdbd}
.foot-brand{left:563px;top:1128px;display:flex;align-items:center;gap:6px;font-family:"Ubuntu",sans-serif;font-size:12px;line-height:12px;color:#bdbdbd}
.foot-brand i{width:24px;height:24px;background:#bdbdbd}
.copyright{left:0;top:1183px;width:768px;text-align:center;font-size:6.5px;color:#fff}
</style>
</head>
<body>
<div class="abs sheet"></div>

<div class="abs brand"><span class="brand-mark"></span><span class="brand-name">Furrow Cover<br>Polls UK</span></div>
<div class="abs search"><span class="search-btn">Search</span></div>

<div class="abs nav-bars"><span style="background:var(--blue)"></span><span style="background:var(--orange)"></span><span style="background:var(--purple)"></span><span style="background:var(--green)"></span><span style="background:var(--grey)"></span></div>
<nav class="abs nav"><span class="current">HOME</span><span>POLICIES</span><span>GLOSSARY</span><span>FACT SHEETS</span><span>SURVEY REPORTS</span><span>NEWS &amp; COMMENT</span></nav>
<div class="abs nav-rule"></div>

<div class="abs slider" role="img" aria-label="Slideshow photo of puppies and kittens facing each other"></div>
<div class="abs slider-arrow" style="left:113px"><svg width="26" height="26"><path d="M15 8l-5 5 5 5" fill="none" stroke="#6a9a5a" stroke-width="2"/></svg></div>
<div class="abs slider-arrow" style="left:626px"><svg width="26" height="26"><path d="M11 8l5 5-5 5" fill="none" stroke="#6a9a5a" stroke-width="2"/></svg></div>
<div class="abs slider-caption">An independent website...dedicated to helping you ...find the best insurance policy...for your pet</div>

<h2 class="abs col-title" style="left:104px;top:334px">Welcome!</h2>
<div class="abs welcome-img" role="img" aria-label="Photo of dogs and cats sitting together"></div>
<div class="abs welcome-text">
  <p>This is an independent website dedicated to helping you to find the best pet insurance policy for your pet</p>
  <p>Here you will find unbiased detailed information about almost all of the 205 pet insurance policies currently available in the UK (we hope the other 3 will follow shortly!)</p>
  <p>We do NOT sell any pet insurance policies nor do we receive commission from any insurance companies</p>
</div>
<div class="abs vrule" style="left:324px;top:336px;height:264px"></div>

<h2 class="abs col-title" style="left:338px;top:334px">Popular Links</h2>
<ul class="abs links">
  <li>Policy Files</li><li>Policy Search</li><li>Fact Sheets</li><li>Policy Listings by Type</li><li>Claims Survey</li><li>2013 Price Survey Report</li>
</ul>
<div class="abs vrule" style="left:470px;top:336px;height:264px"></div>

<h2 class="abs col-title" style="left:499px;top:334px">Check out a Policy</h2>
<div class="abs select" style="top:368px">-- Select Company --</div>
<div class="abs select" style="top:397px">-- Select Policy --</div>
<div class="abs submit">Submit</div>
<div class="abs magnifier" role="img" aria-label="Illustration of a magnifying glass"></div>

<div class="abs hrule"></div>
<div class="abs panel"></div>
<h3 class="abs col-title" style="left:120px;top:636px;font-size:15px">Latest Reviews</h3>
<ul class="abs reviews">
  <li>Review Title 1</li><li>Review Title 2</li><li>Review Title 3</li><li>Review Title 4</li><li>Review Title 5</li><li>Review Title 6</li>
</ul>
<div class="abs vrule" style="left:235px;top:645px;height:155px"></div>
<h3 class="abs col-title" style="left:252px;top:636px;font-size:15px">News &amp; Comment</h3>
<div class="abs news">
  <h4>News Title 1</h4>
  <p>Lorem ipsum dolor sit amet consecutor. Lorem ipsum dolor sit amet consecutor. Lorem ipsum dolor sit amet consecutor. Lorem ipsum dolor sit amet consecutor.</p>
  <a>Read More...</a>
  <h4>News Title 2</h4>
  <p>Lorem ipsum dolor sit amet consecutor. Lorem ipsum dolor sit amet consecutor. Lorem ipsum dolor sit amet consecutor. Lorem ipsum dolor sit amet consecutor.</p>
  <a>Read More...</a>
</div>
<div class="abs news-photo" role="img" aria-label="Photo of a spaniel lying with a cat"></div>

<footer>
<div class="abs footer"></div>
<h3 class="abs foot-title" style="left:95px">Latest Chatterbook Feeds</h3>
<h3 class="abs foot-title" style="left:295px">Latest Tweets</h3>
<h3 class="abs foot-title" style="left:495px">Pet Charities Latest Tweets</h3>

<div class="abs fb">
  <div class="fb-head">Find us on Chatterbook</div>
  <div class="fb-page"><span class="fb-sq"></span><div><div class="fb-name">Chatterbook Platform</div><div class="fb-like">Like</div></div></div>
  <div class="fb-count">2,147,179 people like <b>Chatterbook Platform</b>.</div>
  <div class="fb-grid" role="img" aria-label="Grid of member profile photos">
    <span><i style="background:#d6dbe4"></i>Ruth</span><span><i></i>Tobin</span><span><i style="background:#a59a8e"></i>Rhea</span><span><i style="background:#8f8577"></i>Noor</span><span><i style="background:#9c8f86"></i>Edith</span>
    <span><i style="background:#7c7066"></i>Corin</span><span><i style="background:#a88c73"></i>Lior</span><span><i style="background:#4a4a4a"></i>Mabel</span><span><i style="background:#3a5a3a"></i>Oskar</span><span><i style="background:#7a8896"></i>Pippa</span>
  </div>
  <div class="fb-foot">Chatterbook social plugin</div>
</div>

<div class="abs tweets" style="left:295px">
  <div class="tweet"><svg width="29" height="29"><rect width="29" height="29" fill="#fff"/><circle cx="14.5" cy="11" r="4.5" fill="#1a86d0"/><path d="M6 23c1-5 16-5 17 0z" fill="#1a86d0"/></svg><p><b>Maisiebrook</b> : Lorem ipsum dolor sit amet consecutor. Lorem ipsum dolor sit amet consecutor.<br><em>Wed,22 Apr 2013 22 : 33 : 08</em></p></div>
  <div class="tweet"><svg width="29" height="29"><rect width="29" height="29" fill="#fff"/><circle cx="14.5" cy="11" r="4.5" fill="#1a86d0"/><path d="M6 23c1-5 16-5 17 0z" fill="#1a86d0"/></svg><p><b>Maisiebrook</b> : Lorem ipsum dolor sit amet consecutor. Lorem ipsum dolor sit amet consecutor.<br><em>Wed,22 Apr 2013 22 : 33 : 08</em></p></div>
  <div class="tweet"><svg width="29" height="29"><rect width="29" height="29" fill="#fff"/><circle cx="14.5" cy="11" r="4.5" fill="#1a86d0"/><path d="M6 23c1-5 16-5 17 0z" fill="#1a86d0"/></svg><p><b>Maisiebrook</b> : Lorem ipsum dolor sit amet consecutor. Lorem ipsum dolor sit amet consecutor.<br><em>Wed,22 Apr 2013 22 : 33 : 08</em></p></div>
</div>

<div class="abs tweets" style="left:495px">
  <div class="tweet"><svg width="29" height="29"><rect width="29" height="29" fill="#fff"/><circle cx="14.5" cy="11" r="4.5" fill="#5fb56e"/><path d="M6 23c1-5 16-5 17 0z" fill="#5fb56e"/></svg><p><b>Maisiebrook</b> : Lorem ipsum dolor sit amet consecutor. Lorem ipsum dolor sit amet consecutor.<br><em>Wed,22 Apr 2013 22 : 33 : 08</em></p></div>
  <div class="tweet"><svg width="29" height="29"><rect width="29" height="29" fill="#fff"/><circle cx="14.5" cy="11" r="4.5" fill="#5fb56e"/><path d="M6 23c1-5 16-5 17 0z" fill="#5fb56e"/></svg><p><b>Maisiebrook</b> : Lorem ipsum dolor sit amet consecutor. Lorem ipsum dolor sit amet consecutor.<br><em>Wed,22 Apr 2013 22 : 33 : 08</em></p></div>
  <div class="tweet"><svg width="29" height="29"><rect width="29" height="29" fill="#fff"/><circle cx="14.5" cy="11" r="4.5" fill="#5fb56e"/><path d="M6 23c1-5 16-5 17 0z" fill="#5fb56e"/></svg><p><b>Maisiebrook</b> : Lorem ipsum dolor sit amet consecutor. Lorem ipsum dolor sit amet consecutor.<br><em>Wed,22 Apr 2013 22 : 33 : 08</em></p></div>
</div>

<div class="abs foot-rule" style="top:1064px"></div>
<ul class="abs foot-links" style="left:96px"><li>Link 1</li><li>Link 2</li><li>Link 3</li><li>Link 4</li><li>Link 5</li></ul>
<ul class="abs foot-links" style="left:186px"><li>Link 1</li><li>Link 2</li><li>Link 3</li><li>Link 4</li><li>Link 5</li></ul>
<ul class="abs foot-links" style="left:277px"><li>Link 1</li><li>Link 2</li><li>Link 3</li><li>Link 4</li><li>Link 5</li></ul>
<ul class="abs foot-links" style="left:368px"><li>Link 1</li><li>Link 2</li><li>Link 3</li><li>Link 4</li><li>Link 5</li></ul>
<ul class="abs foot-links" style="left:458px"><li>Link 1</li><li>Link 2</li><li>Link 3</li><li>Link 4</li><li>Link 5</li></ul>
<div class="abs follow">Follow Us On</div>
<div class="abs social"><span></span><span></span><span></span><span></span></div>
<div class="abs foot-brand"><i></i><span>Furrow Cover<br>Polls UK</span></div>
<div class="abs foot-rule" style="top:1173px"></div>
<p class="abs copyright">copyright 2013 © Furrow Cover Polls UK</p>
</footer>
</body>
</html>
```